Business card design for new, innovative company - BluePlinth

We are a new company looking for a business card design that is fun, different and quirky. Must use corporate colour green - CMYK C:55, M:0, Y:100, K:0, and corporate colour grey - C:0, M:0, Y: 0, K:70.

We have developed the first real time data application, in which people are able to profile the data of their existing customers in order to pull out more good fit clients to direct their marketing activities at.

Industry/Entity Type

Marketing

Requirements
Must have
• Logo, name, title, telephone number, fax number, email, website, address

```html
<!DOCTYPE html>
<html lang="en">
<head>
<meta charset="utf-8">
<title>BluePlinth Business Card</title>
<link rel="stylesheet" href="https://fonts.googleapis.com/css2?family=Arimo:wght@400;700&display=swap">
<style>
  :root {
    --brand-green: #7ac143;
    --brand-green-deep: #6cb52d;
    --brand-grey: #58595b;
    --paper: #ffffff;
    --backdrop: #eeeeef;
  }
  * { margin: 0; padding: 0; box-sizing: border-box; }
  html, body {
    width: 1200px;
    height: 981px;
    overflow: hidden;
    background: var(--backdrop);
    font-family: "Arimo", Arial, sans-serif;
  }
  .sheet {
    position: relative;
    width: 1200px;
    height: 981px;
    display: flex;
    align-items: center;
    justify-content: center;
    gap: 60px;
  }
  .card {
    position: relative;
    width: 540px;
    height: 330px;
    overflow: hidden;
    box-shadow: 0 2px 6px rgba(0,0,0,0.12);
  }
  /* Front */
  .card--front {
    background: linear-gradient(160deg, var(--brand-green) 0%, var(--brand-green-deep) 100%);
  }
  .front-disc {
    position: absolute;
    left: 50%;
    top: 50%;
    width: 244px;
    height: 244px;
    margin: -122px 0 0 -122px;
    border-radius: 50%;
    background: var(--paper);
    display: flex;
    align-items: center;
    justify-content: center;
  }
  .wordmark {
    font-weight: 700;
    color: var(--brand-grey);
    letter-spacing: -0.5px;
    display: flex;
    align-items: center;
    gap: 6px;
  }
  .wordmark__dot {
    width: 12px;
    height: 12px;
    border-radius: 50%;
    background: var(--brand-green);
  }
  .front-disc .wordmark { font-size: 34px; }
  /* Back */
  .card--back { background: var(--paper); }
  .back-mark {
    position: absolute;
    left: 190px;
    top: 52px;
    font-size: 32px;
  }
  .name-band {
    position: absolute;
    left: 0;
    top: 108px;
    width: 100%;
    height: 30px;
    background: var(--brand-green);
  }
  .name-band__name {
    position: absolute;
    left: 200px;
    top: 4px;
    color: var(--paper);
    font-weight: 700;
    font-size: 19px;
    letter-spacing: 0.5px;
  }
  .contact-list {
    position: absolute;
    left: 200px;
    top: 160px;
    list-style: none;
    color: var(--brand-grey);
    font-size: 15px;
    line-height: 21px;
  }
  .contact-list li {
    display: flex;
    align-items: flex-start;
    gap: 8px;
  }
  .contact-list svg {
    flex: none;
    width: 12px;
    height: 12px;
    margin-top: 4px;
    fill: var(--brand-grey);
  }
</style>
</head>
<body>
<main class="sheet">
  <section class="card card--front" aria-label="Card front">
    <div class="front-disc">
      <div class="wordmark"><span class="wordmark__dot"></span>BluePlinth</div>
    </div>
  </section>

  <section class="card card--back" aria-label="Card back">
    <div class="wordmark back-mark"><span class="wordmark__dot"></span>BluePlinth</div>
    <div class="name-band"><span class="name-band__name">Lena Hartwell</span></div>
    <ul class="contact-list">
      <li>
        <svg viewBox="0 0 12 12" aria-hidden="true"><path d="M6 0a4 4 0 0 0-4 4c0 3 4 8 4 8s4-5 4-8a4 4 0 0 0-4-4zm0 5.6A1.6 1.6 0 1 1 6 2.4a1.6 1.6 0 0 1 0 3.2z"/></svg>
        <span>27c Fenwick Road, Ely,<br>Cambridgeshire, CB7 4QT</span>
      </li>
      <li>
        <svg viewBox="0 0 12 12" aria-hidden="true"><path d="M3.5 0h5A1 1 0 0 1 9.5 1v10a1 1 0 0 1-1 1h-5a1 1 0 0 1-1-1V1a1 1 0 0 1 1-1zm.3 1.5v7.5h4.4V1.5zM6 9.8a.7.7 0 1 0 0 1.4.7.7 0 0 0 0-1.4z"/></svg>
        <span>07911203546</span>
      </li>
      <li>
        <svg viewBox="0 0 12 12" aria-hidden="true"><circle cx="6" cy="6" r="6"/><path d="M4 3.2l1 1.6-.6.7c.4.9 1.1 1.6 2 2l.7-.6 1.6 1-.6 1.2C5.8 9.1 2.9 6.2 2.9 3.8z" fill="#fff"/></svg>
        <span>01353 480217</span>
      </li>
      <li>
        <svg viewBox="0 0 12 12" aria-hidden="true"><path d="M0 2.5h12v7H0zm1 .8L6 7l5-3.7V3.3H1z"/></svg>
        <span>lena.hartwell@bpdistribution.com</span>
      </li>
      <li>
        <svg viewBox="0 0 12 12" aria-hidden="true"><circle cx="6" cy="6" r="6"/><path d="M1 6h10M6 1c-2 2.5-2 7.5 0 10M6 1c2 2.5 2 7.5 0 10" stroke="#fff" stroke-width="0.9" fill="none"/></svg>
        <span>www.blueplinth.com</span>
      </li>
    </ul>
  </section>
</main>
</body>
</html>
```